Cultural Values, and Purpose, Vision and Mission statements design

We have recently created Cultural Values, and Purpose, Vision and Mission statements for a client’s business. We would like a visual representation created of each of these, to be hung on display in their office. For this project, we would like four (4) graphic design prints drawn up that depict:1. Purpose2. Vision3. Mission4. Cultural ValuesAll print designs should use a recurring, common theme, and be reflective of the business’ colours (see attached logo.)Please read and follow specifications in attached design brief.
Updates

Need extra days to review

Target Market(s)

Females, aged between 37 and 57 years old, who are family orientated, living locally, married and have between 1 and 3 children living at home.

Requirements
Must have
• Photoshop (PSD) format: All completed design will need to be in Photoshop (PSD) format before being handed over. This is to ensure that we can make alterations before printing if necessary.
• Quality: All designs must be 300 pixels resolution or higher.
• Purpose, Vision & Mission Designs Dimensions: The dimensions for each of the Purpose, Vision and Mission designs will need to be 30.5cm x 40.6cm (portrait, rectangle shape) with a surrounding 3.8cm border as it will be printed onto canvas matching these specifications.
• Cultural Values Dimensions: There are no specific dimensions required for the Cultural Values so the designer should feel free to display them best they see fit.
• Theme: All must follow the same theme and be reflective of the business's colours and logo.

```html
<!DOCTYPE html>
<html lang="en">
<head>
<meta charset="utf-8">
<title>Vision – Valleyway Motors</title>
<link href="https://fonts.googleapis.com/css2?family=Marcellus&family=Questrial&family=Montserrat:wght@500&display=swap" rel="stylesheet">
<style>
  :root {
    --orange: #f5a316;
    --brand-orange: #ee7a22;
    --band-dark: #2f3533;
    --band-mid: #45403f;
    --white: #ffffff;
    --shadow: #1c1c1c;
    --wood-light: #eed3b4;
    --wood-dark: #d9b48e;
    --vision-shade: #9a9a9a;
  }
  html, body {
    margin: 0;
    padding: 0;
    overflow: hidden;
  }
  .poster {
    position: relative;
    width: 902px;
    height: 1200px;
    background: var(--orange);
    overflow: hidden;
    font-family: "Questrial", sans-serif;
  }
  .brand-plate {
    position: absolute;
    left: 18px;
    top: 19px;
    width: 450px;
    height: 89px;
    background: var(--white);
    box-shadow: -3px 3px 0 var(--shadow);
    display: flex;
    align-items: center;
    gap: 14px;
    padding-left: 26px;
    box-sizing: border-box;
  }
  .brand-mark {
    width: 22px;
    height: 22px;
    background: var(--brand-orange);
    flex: none;
  }
  .brand-name {
    font-family: "Montserrat", sans-serif;
    font-weight: 500;
    font-size: 40px;
    color: var(--brand-orange);
    letter-spacing: 0.5px;
  }
  .hand-figure {
    position: absolute;
    left: 350px;
    top: 365px;
    width: 202px;
    height: 628px;
    border-radius: 60px 60px 20px 20px;
    background: linear-gradient(90deg, var(--wood-dark), var(--wood-light) 45%, var(--wood-dark));
  }
  .statement-band {
    position: absolute;
    left: 0;
    top: 996px;
    width: 902px;
    height: 182px;
  }
  .statement-title {
    position: absolute;
    left: 11px;
    top: 1030px;
    margin: 0;
    font-family: "Marcellus", serif;
    font-weight: 400;
    font-size: 104px;
    line-height: 1;
    color: var(--white);
    text-shadow: 4px 2px 0 var(--vision-shade);
    letter-spacing: 1px;
  }
  .statement-divider {
    position: absolute;
    left: 352px;
    top: 1022px;
    width: 2px;
    height: 122px;
    background: var(--white);
  }
  .statement-text {
    position: absolute;
    left: 368px;
    top: 1022px;
    margin: 0;
    color: var(--white);
    width: 520px;
  }
  .statement-text .line {
    display: block;
    white-space: nowrap;
  }
  .statement-text .small { font-size: 21px; line-height: 27px; }
  .statement-text .large { font-size: 26px; line-height: 34px; }
</style>
</head>
<body>
<div class="poster">
  <div class="brand-plate">
    <span class="brand-mark"></span>
    <span class="brand-name">Valleyway Motors</span>
  </div>

  <div class="hand-figure" role="img" aria-label="Photograph of a wooden artist's mannequin hand raising its index finger"></div>

  <svg class="statement-band" viewBox="0 996 902 182" width="902" height="182" aria-hidden="true">
    <defs>
      <linearGradient id="bandFill" x1="0" y1="0" x2="1" y2="0">
        <stop offset="0" stop-color="#333a38"/>
        <stop offset="0.35" stop-color="#4a4140"/>
        <stop offset="1" stop-color="#2c3431"/>
      </linearGradient>
    </defs>
    <polygon points="0,1000 862,1000 902,1087 862,1174 0,1174" fill="url(#bandFill)"/>
    <polyline points="0,1010 852,1010 886,1087 852,1158 0,1158" fill="none" stroke="var(--brand-orange)" stroke-width="3"/>
    <polyline points="0,1001 862,1001 901,1087 862,1173 0,1173" fill="none" stroke="var(--band-mid)" stroke-width="2"/>
  </svg>

  <h1 class="statement-title">VISION</h1>
  <div class="statement-divider"></div>
  <p class="statement-text">
    <span class="line small">We will earn our reputation for being</span>
    <span class="line small">the number one,</span>
    <span class="line large">family focused, automotive specialists</span>
    <span class="line small">throughout the <span class="large">Latrobe Valley.</span></span>
  </p>
</div>
</body>
</html>
```